Grand Bridal Pastry Selling Method needs finishing touches to website.

We have a temporary website located at http://www.brivantaworks.example/qk/.
We are doing a responsive design and have created the architecture (layout). However, we need a professional makeover for the graphic elements and colors of the website. The website will be selling a sales course to mostly women who sell wedding cakes.
The photos within the posted website are for illustrative purposes. We will use our own photos after the website is redone.
We are open to changing the font styles, borders, header, and anything else as long as the layout is not changed.
Target Market(s)
75% women age 25-50 and men 30-60.
Industry/Entity Type
Architecture
Colors
Designer to choose colors to be used in the design.
Look and feel
Each slider illustrates characteristics of the customer's brand and the style your logo design should communicate.

```html
<!DOCTYPE html>
<html lang="en">
<head>
<meta charset="utf-8">
<title>Grand Bridal Pastry Selling Method</title>
<link href="https://fonts.googleapis.com/css2?family=Open+Sans:ital,wght@0,600;0,700;1,600;1,700&family=Source+Sans+3:ital,wght@1,600;1,700&family=Arimo:wght@700&display=swap" rel="stylesheet">
<style>
  :root {
    --page: #ffffff;
    --green: #7cb75a;
    --lime: #c9d72b;
    --ink: #1c1c1c;
    --dark-band: #3a3a3c;
    --card: #eceeed;
    --video: #050505;
    --bg-light: #d9dcd8;
    --bg-blue: #a9bcc0;
    --bg-warm: #b7aca2;
    --mark: #b9b9b9;
  }
  * { box-sizing: border-box; margin: 0; padding: 0; }
  html, body { width: 1132px; height: 1200px; overflow: hidden; }
  body { position: relative; font-family: "Open Sans", Arial, sans-serif; color: var(--ink); }

  .backdrop {
    position: absolute; inset: 0;
    background:
      radial-gradient(ellipse at 12% 40%, var(--bg-blue) 0%, transparent 45%),
      radial-gradient(ellipse at 92% 50%, #eef0ee 0%, transparent 40%),
      radial-gradient(ellipse at 50% 95%, #e6e6e4 0%, transparent 55%),
      linear-gradient(180deg, var(--bg-warm) 0%, var(--bg-light) 60%, #c9c9c6 100%);
  }

  .page { position: absolute; left: 133px; top: 32px; width: 830px; height: 1093px; background: var(--page); }

  .site-title {
    position: absolute; left: 41px; top: 46px; width: 650px;
    font-family: "Source Sans 3", "Open Sans", Arial, sans-serif;
    font-size: 22px; font-weight: 700; font-style: italic; letter-spacing: -0.1px;
    white-space: nowrap;
  }
  .header-photo {
    position: absolute; left: 739px; top: 18px; width: 63px; height: 89px;
    background: linear-gradient(180deg, #f2f0e8 0%, #e4e6d8 60%, #9fb378 100%);
    border-radius: 30px 30px 6px 6px;
  }

  .main-nav {
    position: absolute; left: 6px; top: 109px; width: 813px; height: 30px;
    background: var(--green); display: flex;
  }
  .main-nav a {
    color: #fff; text-decoration: none; font-size: 12.5px; font-weight: 600;
    display: flex; align-items: center; justify-content: center;
    border-right: 1.5px solid #fff; white-space: nowrap;
  }
  .main-nav a:nth-child(1) { width: 112px; }
  .main-nav a:nth-child(2) { width: 110px; }
  .main-nav a:nth-child(3) { width: 228px; }
  .main-nav a:nth-child(4) { width: 101px; }

  .video-frame { position: absolute; left: 6px; top: 148px; width: 539px; height: 327px; background: var(--video); }

  .optin {
    position: absolute; left: 559px; top: 148px; width: 260px; height: 327px;
    background: var(--lime); color: #fff;
  }
  .optin h2 {
    text-align: center; font-style: italic; font-weight: 700; font-size: 21px; line-height: 29px;
    margin-top: 14px;
  }
  .optin label { position: absolute; left: 32px; font-size: 17px; font-style: italic; font-weight: 700; }
  .optin .field { position: absolute; left: 32px; width: 188px; height: 23px; background: #fff; border: none; }
  .optin .submit {
    position: absolute; left: 70px; top: 264px; width: 118px; height: 21px;
    background: var(--green); color: #fff; border: none;
    font: 700 10px "Open Sans", Arial, sans-serif;
  }
  .optin .promise { position: absolute; left: 0; width: 100%; top: 293px; text-align: center; font-size: 11px; font-weight: 700; }

  .section-bar {
    position: absolute; left: 6px; top: 498px; width: 804px; height: 40px;
    background: var(--dark-band); color: #fff;
    font-size: 13px; font-style: italic; font-weight: 700;
    display: flex; align-items: center; padding-left: 16px; white-space: nowrap;
  }

  .technique { position: absolute; top: 561px; width: 185px; height: 318px; background: var(--card); }
  .technique .photo { width: 100%; height: 116px; }
  .technique p {
    font-family: "Arimo", Arial, sans-serif; font-weight: 700; font-size: 10.5px; line-height: 13px;
    padding: 0 8px 0 9px; margin-top: 10px;
  }
  .technique p + p { margin-top: 21px; }
  .technique .read-more {
    position: absolute; left: 15px; top: 277px;
    font-family: "Arimo", Arial, sans-serif; font-weight: 700; font-size: 12px; color: var(--ink); text-decoration: none;
  }

  .press { position: absolute; left: 0; top: 925px; width: 830px; height: 40px; }
  .press span { position: absolute; top: 6px; height: 28px; background: var(--mark); opacity: 0.55; }

  .site-footer {
    position: absolute; left: 9px; top: 1022px; width: 821px; height: 71px;
    background: var(--dark-band); color: #fff;
  }
  .site-footer .copy { position: absolute; right: 20px; top: 13px; font-size: 14px; font-weight: 600; white-space: nowrap; }
  .site-footer nav { position: absolute; right: 20px; top: 44px; display: flex; gap: 30px; }
  .site-footer nav a { color: #fff; text-decoration: none; font-size: 12px; font-weight: 600; white-space: nowrap; }
</style>
</head>
<body>
  <div class="backdrop" role="img" aria-label="Soft blurred photograph of white and pale blue wedding cakes"></div>

  <main class="page">
    <h1 class="site-title">Cracking The “Secret Code” That Unlocks Your Wedding Cake Sales!</h1>
    <div class="header-photo" role="img" aria-label="Small tiered wedding cake with green flowers"></div>

    <nav class="main-nav">
      <a href="#">home</a>
      <a href="#">Who is lars brenner</a>
      <a href="#">Why lars is sharing his secrets</a>
      <a href="#">Contact</a>
    </nav>

    <div class="video-frame" role="img" aria-label="Video player"></div>

    <form class="optin">
      <h2>Free Videos To Help<br>You Sell More Wedding<br>Cakes At Higher<br>Prices Inmmediately</h2>
      <label style="top:154px">Name</label>
      <input class="field" style="top:181px" type="text" aria-label="Name">
      <label style="top:212px">Email</label>
      <input class="field" style="top:237px" type="text" aria-label="Email">
      <button class="submit" type="button">get instant access</button>
      <div class="promise">No spam I promise</div>
    </form>

    <div class="section-bar">3 Leading Edge Techniques For Convincing Brides To Choose You</div>

    <article class="technique" style="left:22px">
      <div class="photo" role="img" aria-label="Tiered white cake with red roses" style="background:linear-gradient(160deg,#e9e2da,#c9b6ab 60%,#8f3b4a)"></div>
      <p>In the firs video, discover a sales growth secret that reveals the two faces of your wedding cake business.</p>
      <p>One side of your face displays your internal reality, it's how you run your business whether....</p>
      <a class="read-more" href="#">Read More</a>
    </article>
    <article class="technique" style="left:223px">
      <div class="photo" role="img" aria-label="Tall white cake with pink flower cascade" style="background:linear-gradient(160deg,#efefed,#dcd3d2 60%,#c8a0a6)"></div>
      <p>In the firs video, discover a sales growth secret that reveals the two faces of your wedding cake business.</p>
      <p>One side of your face displays your internal reality, it's how you run your business whether....</p>
      <a class="read-more" href="#">Read More</a>
    </article>
    <article class="technique" style="left:424px">
      <div class="photo" role="img" aria-label="Ivory beaded cake with peach flowers" style="background:linear-gradient(160deg,#8a8a86,#d8d4cc 55%,#c9b19c)"></div>
      <p>In the firs video, discover a sales growth secret that reveals the two faces of your wedding cake business.</p>
      <p>One side of your face displays your internal reality, it's how you run your business whether....</p>
      <a class="read-more" href="#">Read More</a>
    </article>
    <article class="technique" style="left:625px">
      <div class="photo" role="img" aria-label="Baker decorating a white tiered cake" style="background:linear-gradient(160deg,#6f6a62,#cfc9c0 55%,#efeeea)"></div>
      <p>In the firs video, discover a sales growth secret that reveals the two faces of your wedding cake business.</p>
      <p>One side of your face displays your internal reality, it's how you run your business whether....</p>
      <a class="read-more" href="#">Read More</a>
    </article>

    <div class="press" aria-label="Featured in">
      <span style="left:47px;width:38px"></span>
      <span style="left:146px;width:112px;height:16px;top:12px"></span>
      <span style="left:312px;width:36px;border-radius:50%"></span>
      <span style="left:460px;width:42px"></span>
      <span style="left:571px;width:93px;opacity:0.8"></span>
      <span style="left:716px;width:80px;height:22px;top:9px"></span>
    </div>

    <footer class="site-footer">
      <div class="copy">Copyright © 2014 The Sugar Atelier. Phone: 555.014.2290. All Rights Reserved.</div>
      <nav>
        <a href="#">Home</a>
        <a href="#">Who Is Lars Brenner</a>
        <a href="#">Why Lars Is Sharing His Secrets</a>
        <a href="#">Contact</a>
      </nav>
    </footer>
  </main>
</body>
</html>
```